Education Offering Flyer

Design a simple and clean A4 flyer, front and back, that presents our sales offering in an attractive way. The flyer consists of a title, a sub-heading, bullet points, paragraphed content and a small diagram with a caption.The design needs to be consistent with the style of the PowerPoint presentation that is attached.

We are a company that provides education software solutions for districts, schools, teachers, and students. We have a portfolio of products and services. Our offerings combine our products and services in different ways to address different education needs.

The target audience of this flyer is a decision-maker in an education organization.

Specifications:

Design a double-sided A4 flyer
Maintain our corporate logo color theme and tones (orange, blue, green, white, grey)
Follow PPTX style/theme (fonts, circles, squares, boxes)
Deliver a professional (business), clean, and modern look
Use photos that are relevant e.g. school and students with devices and technology [Optional]
Include icons [Optional]

I would like to receive the final file as a PSD format for hard copy printing. But for the purpose of review, a JPEG would be suitable.

Industry/Entity Type

Education

```html
<!DOCTYPE html>
<html lang="en">
<head>
<meta charset="utf-8">
<title>Lumora Education – LMS Flyer</title>
<link href="https://fonts.googleapis.com/css2?family=Oswald:wght@500;700&family=Open+Sans:wght@400;600;700&family=Cormorant+Garamond:ital,wght@1,600&display=swap" rel="stylesheet">
<style>
  :root{
    --orange:#ee7a1f;
    --orange-dark:#d9650f;
    --green:#4ea63a;
    --green-dark:#3c8c2b;
    --grey:#d6d7d9;
    --grey-dark:#8c8f93;
    --white:#ffffff;
    --ink:#3a3a3a;
    --stage:#e8e5e0;
    --diagram-line:#c0392b;
  }
  *{box-sizing:border-box;margin:0;padding:0}
  html,body{width:1200px;height:1000px;overflow:hidden;background:var(--stage)}
  body{position:relative;font-family:"Open Sans",Arial,sans-serif;color:var(--white)}
  .page{position:absolute;top:118px;width:540px;height:764px;background:var(--white);overflow:hidden;box-shadow:0 6px 24px rgba(0,0,0,.18)}
  .page--back{left:40px}
  .page--front{left:620px}

  .photo{position:absolute}

  /* footer shared */
  .footer{position:absolute;left:0;right:0;bottom:0;height:124px;background:linear-gradient(180deg,var(--white) 0 40%,var(--grey) 40% 100%)}
  .footer__legal{position:absolute;left:22px;bottom:18px;font-size:7px;line-height:1.5;color:var(--grey-dark)}
  .footer__right{position:absolute;right:22px;bottom:18px;display:flex;align-items:center;gap:14px}
  .footer__web{font-size:7px;line-height:1.5;color:var(--grey-dark);text-align:right;white-space:nowrap}
  .brand{display:flex;align-items:center;gap:6px}
  .brand__dot{width:20px;height:20px;border-radius:50%;background:var(--green);flex:none}
  .brand__name{font-family:"Open Sans",Arial,sans-serif;font-weight:700;font-size:14px;color:var(--orange);letter-spacing:.5px;white-space:nowrap}

  /* back page */
  .facts{position:absolute;left:0;top:0;width:250px;height:640px;background:var(--orange);padding:22px 20px 0 22px}
  .facts__title{font-family:"Oswald",Impact,sans-serif;font-weight:700;font-size:30px;letter-spacing:1px;margin-bottom:12px}
  .facts__item{font-size:9.5px;line-height:1.45;margin-bottom:8px}
  .facts__label{font-family:"Oswald",Impact,sans-serif;font-weight:500;font-size:12px;color:#fff3c4;margin-right:3px}
  .photo--classroom{left:250px;top:0;width:290px;height:250px;background:linear-gradient(160deg,#c9d3e0,#8fa6c2 45%,#5f7090 80%,#4f5e78)}
  .photo--reader{left:20px;top:420px;width:225px;height:250px;z-index:2;background:radial-gradient(ellipse at 50% 40%,#f3d9b0,#e3b96f 45%,#b8733b 80%,rgba(184,115,59,0) 100%)}
  .order{position:absolute;left:250px;top:250px;width:290px;height:390px;background:var(--green);padding:18px 20px}
  .order__text{font-size:9.5px;line-height:1.5}
  .diagram{position:absolute;left:22px;top:120px;width:250px;height:180px;background:linear-gradient(180deg,#ffffff,#eeeeee);border:1px solid #cfcfcf}
  .diagram text{font-family:"Open Sans",Arial,sans-serif;font-size:7px;fill:#fff;font-weight:600}

  /* front page */
  .photo--students{left:0;top:0;width:540px;height:430px;background:linear-gradient(135deg,#2d4a3c,#3e6a55 40%,#9fb9c7 70%,#4a6a5a)}
  .ribbon{position:absolute;left:230px;top:300px;width:310px;height:82px;background:linear-gradient(90deg,rgba(78,166,58,.92),rgba(60,140,43,.75));transform:skewY(8deg);padding:12px 20px}
  .ribbon__line{font-family:"Cormorant Garamond",Georgia,serif;font-style:italic;font-weight:600;font-size:24px;line-height:1.05;color:var(--white);transform:skewY(-8deg)}
  .ribbon__line--second{padding-left:60px}
  .intro{position:absolute;left:0;top:400px;width:250px;height:240px;background:var(--orange);padding:16px 20px}
  .intro__title{font-family:"Oswald",Impact,sans-serif;font-weight:700;font-size:20px;line-height:1.1;text-transform:uppercase;margin-bottom:10px}
  .intro__lead{font-size:10.5px;line-height:1.45}
  .photo--study{left:18px;top:560px;width:150px;height:150px;z-index:2;border-radius:50%;border:5px solid var(--white);background:radial-gradient(circle at 45% 40%,#e8d2b8,#b98a62 55%,#7a5a48);box-shadow:0 2px 6px rgba(0,0,0,.2)}
  .benefits{position:absolute;left:250px;top:420px;width:290px;height:220px;background:var(--green);padding:16px 18px}
  .benefits__lead{font-size:10px;font-weight:700;line-height:1.45;margin-bottom:8px}
  .benefits__text{font-size:7.5px;line-height:1.5;margin-bottom:7px}
</style>
</head>
<body>

<section class="page page--back" aria-label="Flyer back: fast facts">
  <div class="facts">
    <h2 class="facts__title">FAST FACTS</h2>
    <p class="facts__item"><span class="facts__label">Who:</span>K-12 schools, network of schools, districts and states.</p>
    <p class="facts__item"><span class="facts__label">What:</span>Manage teaching and learning workflows.</p>
    <p class="facts__item"><span class="facts__label">Why:</span>A unified system for digital work, collaboration and communication between teachers, students, parents and administrators.</p>
    <p class="facts__item"><span class="facts__label">Aspects:</span>Assignments, Lesson Plans, Gradebook, Quizzes, Attendance, Discussions, Calendar, Messaging, Parent Portal and Administration.</p>
    <p class="facts__item"><span class="facts__label">Dependencies:</span>None</p>
    <p class="facts__item"><span class="facts__label">Integration:</span>Third-party SMS/SIS, content management systems, school websites and portals.</p>
  </div>

  <div class="photo photo--classroom" role="img" aria-label="Photo of smiling students at desks in a classroom"></div>

  <div class="order">
    <p class="order__text">Bringing Order. With so many acronyms, understanding technology can feel like an alphabet soup. But with the right learning management system, alphabet soup turns into alphabetical order. Integration of student and content management systems and other tools provide a hub for students and educators to log in, track their work and easily communicate.</p>
    <svg class="diagram" viewBox="0 0 250 180" role="img" aria-label="Diagram: LMS connected to LCMS, SIS, website and other tools">
      <g stroke="var(--diagram-line)" stroke-width="1" stroke-dasharray="3 2" fill="none">
        <path d="M55 38 V88 H95"/>
        <path d="M165 38 V80"/>
        <path d="M160 92 H205"/>
        <path d="M125 100 V130 H60 V142"/>
      </g>
      <rect x="25" y="22" width="58" height="20" rx="3" fill="var(--orange)"/>
      <text x="54" y="35" text-anchor="middle">LCMS</text>
      <rect x="138" y="16" width="62" height="26" rx="3" fill="var(--orange)"/>
      <text x="169" y="27" text-anchor="middle">Other tools such</text>
      <text x="169" y="36" text-anchor="middle">as Office suites</text>
      <rect x="92" y="80" width="70" height="20" rx="3" fill="var(--green)"/>
      <text x="127" y="93" text-anchor="middle">LMS</text>
      <rect x="198" y="82" width="42" height="20" rx="3" fill="var(--orange)"/>
      <text x="219" y="95" text-anchor="middle">SIS</text>
      <rect x="30" y="140" width="58" height="20" rx="3" fill="var(--orange)"/>
      <text x="59" y="153" text-anchor="middle">Website</text>
    </svg>
  </div>

  <div class="photo photo--reader" role="img" aria-label="Photo of a girl reading while sitting on a stack of books"></div>

  <footer class="footer">
    <p class="footer__legal">Lumora Education · Advancing the future of K-12 learning<br>© Copyright 2014 Lumora. All rights reserved.</p>
    <div class="footer__right">
      <p class="footer__web">www.lumoralearn.com</p>
      <div class="brand"><span class="brand__dot"></span><span class="brand__name">LUMORA EDUCATION</span></div>
    </div>
  </footer>
</section>

<section class="page page--front" aria-label="Flyer front: the right learning management system">
  <div class="photo photo--students" role="img" aria-label="Photo of four smiling teenage students in front of a chalkboard"></div>
  <div class="ribbon">
    <p class="ribbon__line">Student Success</p>
    <p class="ribbon__line ribbon__line--second">Enjoy Learning</p>
  </div>

  <div class="intro">
    <h1 class="intro__title">The Right Learning Management System</h1>
    <p class="intro__lead">Managing teaching and learning workflows has never been smoother with Lumora Education LMS.</p>
  </div>

  <div class="benefits">
    <p class="benefits__lead">Teachers and students certainly have enough to worry about without having to focus on technology. Quizzes, tests, grading, instruction time, assignments — the list goes on.</p>
    <p class="benefits__text">When a smooth and reliable technology system is in place, the focus can stay on teaching and learning. Teachers can create and share lessons in minutes, students find their work in one place, and parents follow progress without extra calls or paper. Everything is organised, secure and ready whenever the school day begins.</p>
    <p class="benefits__text">The right learning management system brings a smooth and efficient workflow to every classroom. With clear tools for planning, grading and feedback, Lumora Education LMS gives districts one reliable platform that grows with their schools and keeps every learner moving forward.</p>
  </div>

  <div class="photo photo--study" role="img" aria-label="Round photo of two students working at a desk"></div>

  <footer class="footer">
    <p class="footer__legal">Lumora Education · Advancing the future of K-12 learning<br>© Copyright 2014 Lumora. All rights reserved.</p>
    <div class="footer__right">
      <p class="footer__web">www.lumoralearn.com</p>
      <div class="brand"><span class="brand__dot"></span><span class="brand__name">LUMORA EDUCATION</span></div>
    </div>
  </footer>
</section>

</body>
</html>
```